Custom unique Stationary design for Logistics company

We need a custom, unique , elegant and luxurious full stationary design using our new logo, following these guidelines:
1- Business card: double sided, both sides uses the navy blue as the background main color (same as the code of the navy blue used in our logo).
2- envelope and folder: also use the same navy blue as the main background color.
3- book cover( notepad cover) : same thing with the navy blue
4- letterhead: feel free to use the combination of the colors in our logo.
5- rest of the items are up to your creativity

Target Market(s)

corporates and other businesses

Industry/Entity Type

Logistics and heavy machines contractors

Requirements
Must have
• Letterhead, business card, envelope, notepad cover, paper, file
Nice to have
• navy blue to be main background color for business card, envelope, notepad cover

```html
<!DOCTYPE html>
<html lang="en">
<head>
<meta charset="utf-8">
<title>Harborline Freight — Stationery</title>
<link href="https://fonts.googleapis.com/css2?family=Montserrat:wght@400;500;800&family=Roboto:wght@400;500&display=swap" rel="stylesheet">
<style>
  :root{
    --navy:#0f3f6f;
    --cover:#1a5580;
    --orange:#e8572a;
    --blush:#efc3b6;
    --mauve:#6a5c6e;
    --grey:#8a8f99;
    --paper:#f1f1ef;
    --ink:#1d1d1f;
    --backdrop:#e4e4e6;
  }
  *{box-sizing:border-box;margin:0;padding:0}
  html,body{width:1200px;height:792px;overflow:hidden}
  body{position:relative;background:var(--backdrop);font-family:"Roboto",sans-serif}
  .sheet{position:absolute;box-shadow:0 6px 14px rgba(0,0,0,.18);overflow:hidden}
  .wordmark{font-family:"Montserrat",sans-serif;font-weight:800;color:var(--navy);line-height:1;letter-spacing:.01em;white-space:nowrap}
  .wordmark--light{color:#fff}

  /* business cards */
  .card{top:137px;width:135px;height:78px;background:var(--navy);display:flex;align-items:center}
  .card--front{left:62px;justify-content:center}
  .card--front .wordmark{font-size:12px}
  .card--back{left:218px;padding:0 6px}
  .card--back .wordmark{font-size:8px;width:58px;white-space:normal;text-align:center}
  .card__rule{width:1px;height:36px;background:rgba(255,255,255,.5);margin:0 6px;flex:none}
  .card__details{font-family:"Montserrat",sans-serif;color:#fff;font-size:2.6px;line-height:4.2px}
  .card__name{color:var(--orange);font-size:5px;font-weight:500;line-height:5px}
  .card__title{font-size:3.4px;margin-bottom:4px;line-height:4px}

  /* envelopes */
  .envelope{left:62px;width:291px;height:145px;background:var(--paper)}
  .envelope--back{top:236px;padding:16px}
  .envelope--back .wordmark{font-size:10px;position:relative}
  .envelope__wash{position:absolute;right:0;top:0;width:90px;height:100%;
    background:radial-gradient(ellipse 80% 60% at 70% 50%,rgba(239,195,182,.75),rgba(239,195,182,.25) 60%,rgba(239,195,182,0) 100%)}
  .envelope--front{top:406px}
  .envelope__flap{height:37px;background:var(--navy);border-radius:0 0 8px 8px;margin:0 3px;display:flex;align-items:center;justify-content:center}
  .envelope__flap .wordmark{font-size:11px}

  /* letterhead */
  .letterhead{left:385px;top:131px;width:367px;height:519px;background:var(--paper);padding:0 57px}
  .letterhead__logo{text-align:center;padding-top:88px}
  .letterhead__logo .wordmark{font-size:21px}
  .letter{margin-top:77px;font-size:6.4px;line-height:11px;color:var(--ink);text-align:justify}
  .letter p{margin-bottom:11px}
  .letter .strong{font-weight:500}
  .letter__sign{width:95px;height:34px;background:linear-gradient(90deg,rgba(232,87,42,.18),rgba(232,87,42,.08));margin-top:6px;border-radius:3px}
  .letter-footer{position:absolute;left:37px;right:40px;bottom:25px;display:flex;justify-content:space-between;font-family:"Montserrat",sans-serif;font-size:8px;line-height:10px;color:var(--navy)}
  .letter-footer li{list-style:none;display:flex;align-items:center;gap:3px}
  .letter-footer svg{width:6px;height:6px;flex:none}
  .address{display:flex;gap:3px}
  .address svg{margin-top:2px}

  /* notebook */
  .notebook{left:789px;top:131px;width:361px;height:514px;background:var(--cover);overflow:visible}
  .notebook__wash{position:absolute;right:0;top:0;width:110px;height:100%;
    background:radial-gradient(ellipse 90% 55% at 85% 50%,rgba(106,92,110,.85),rgba(106,92,110,.35) 60%,rgba(106,92,110,0) 100%)}
  .notebook__spine{position:absolute;left:42px;top:0;bottom:0;width:1px;background:rgba(0,0,0,.25)}
  .notebook__rings{position:absolute;left:-11px;top:12px;bottom:12px;display:flex;flex-direction:column;justify-content:space-between}
  .ring{display:block;width:37px;height:9px;position:relative}
  .ring::before{content:"";position:absolute;left:0;top:2px;width:31px;height:5px;border-radius:3px;background:#151515}
  .ring::after{content:"";position:absolute;right:0;top:0;width:9px;height:9px;border-radius:50%;background:#d8dadd;box-shadow:inset 2px 0 0 #111}
  .notebook__brand{position:absolute;left:42px;right:0;top:205px;text-align:center}
  .notebook__brand .wordmark{font-size:25px}
  .notebook__url{margin-top:58px;font-family:"Montserrat",sans-serif;font-size:9.5px;color:#fff}
  .notebook__url span{color:var(--orange)}
</style>
</head>
<body>

  <section class="sheet card card--front" aria-label="Business card front">
    <span class="wordmark wordmark--light">Harborline Freight</span>
  </section>

  <section class="sheet card card--back" aria-label="Business card back">
    <span class="wordmark wordmark--light">Harborline Freight</span>
    <span class="card__rule"></span>
    <div class="card__details">
      <div class="card__name">Dalia R. Okafor</div>
      <div class="card__title">President</div>
      <div>555-201-3380</div>
      <div>dalia.okafor@harborline.example</div>
      <div>www.harborlinefreight.example</div>
      <div>220 Quarry Lane, Ridgeford, WI 53000</div>
    </div>
  </section>

  <section class="sheet envelope envelope--back" aria-label="Envelope">
    <div class="envelope__wash" role="img" aria-label="Faint large brand decoration in soft coral"></div>
    <span class="wordmark">Harborline Freight</span>
  </section>

  <section class="sheet envelope envelope--front" aria-label="Envelope with flap">
    <div class="envelope__flap"><span class="wordmark wordmark--light">Harborline Freight</span></div>
  </section>

  <article class="sheet letterhead" aria-label="Letterhead">
    <header class="letterhead__logo"><span class="wordmark">Harborline Freight</span></header>
    <div class="letter">
      <p class="strong">Dear Customers,</p>
      <p>Lorem ipsum dolor sit amet, consectetur adipiscing elit. Nunc varius, lectus vel eleifend vulputate, tortor diam sollicitudin mauris, vitae finibus diam est at sem. Aliquam mattis in mauris vel porta. Praesent volutpat lacus non massa sagittis, id eleifend sapien vestibulum. Etiam pretium odio rutrum semper scelerisque. Vestibulum tortor ligula, bibendum non dictum vitae, luctus eget massa.</p>
      <p style="margin-top:22px">Lorem ipsum dolor sit amet, consectetur adipiscing elit. Suspendisse dapibus nunc eu molestie condimentum. Sed quis dolor non lorem lobortis convallis. Sed pretium erat ac tellus dapibus tempus. Maecenas semper erat id dictum tempor. Sed quis urna a orci luctus porta. Nam tempus libero mollis erat gravida, eget ullamcorper tortor commodo.</p>
      <p>Maecenas semper erat id dictum tempor. Sed quis urna a orci luctus porta. Nam tempus libero mollis erat gravida, eget ullamcorper tortor commodo.</p>
      <p class="strong">Sincerely yours,</p>
      <div class="letter__sign" role="img" aria-label="Handwritten signature"></div>
    </div>
    <footer class="letter-footer">
      <ul>
        <li><svg viewBox="0 0 10 10"><path d="M2 1l2 2-1 1.5c.6 1.2 1.3 1.9 2.5 2.5L7 6l2 2-1.5 1.5C4.5 9 1 5.5.5 2.5z" fill="var(--orange)"/></svg>555-201-3380</li>
        <li><svg viewBox="0 0 10 10"><rect x="1" y="2" width="8" height="6" fill="none" stroke="var(--orange)"/><path d="M1 2l4 3.5L9 2" fill="none" stroke="var(--orange)"/></svg>dalia.okafor@harborline.example</li>
        <li><svg viewBox="0 0 10 10"><circle cx="5" cy="5" r="4" fill="none" stroke="var(--orange)"/><path d="M1 5h8M5 1c-2 2.5-2 5.5 0 8M5 1c2 2.5 2 5.5 0 8" fill="none" stroke="var(--orange)" stroke-width=".7"/></svg>www.harborlinefreight.example</li>
      </ul>
      <div class="address">
        <svg viewBox="0 0 10 10"><path d="M5 9.5S1.5 5.5 1.5 3.5a3.5 3.5 0 0 1 7 0C8.5 5.5 5 9.5 5 9.5z" fill="none" stroke="var(--orange)"/><circle cx="5" cy="3.5" r="1.2" fill="var(--orange)"/></svg>
        <div>220 Quarry Lane<br>Ridgeford,<br>WI 53000</div>
      </div>
    </footer>
  </article>

  <section class="sheet notebook" aria-label="Notepad cover">
    <div class="notebook__wash" role="img" aria-label="Large faint brand decoration in muted mauve"></div>
    <div class="notebook__rings">
      <span class="ring"></span><span class="ring"></span><span class="ring"></span><span class="ring"></span>
      <span class="ring"></span><span class="ring"></span><span class="ring"></span><span class="ring"></span>
      <span class="ring"></span><span class="ring"></span><span class="ring"></span><span class="ring"></span>
      <span class="ring"></span><span class="ring"></span><span class="ring"></span><span class="ring"></span>
      <span class="ring"></span>
    </div>
    <div class="notebook__spine"></div>
    <div class="notebook__brand">
      <span class="wordmark wordmark--light">Harborline Freight</span>
      <div class="notebook__url">www.<span>harborlinefreight</span>.example</div>
    </div>
  </section>

</body>
</html>
```